依頼詳細
企画内容や入れた欲しい文言は添付資料にあります。(A4で2枚分)
文字の大きさや赤字は私が強調したいと考えているイメージと捉えてください。
また、文言・キャッチ等の変更の提案は大歓迎です。是非勉強させてください!

イメージしている事
・女性がターゲットになっているような雰囲気。
・当たり障りのないというよりは、どこか振り切れているような個性的な雰囲気。
・「頑張ってやってくれそうね。」という印象を持ってもらいたい。
今回ワークテラスさんに依頼するのは、2回目ですが前回(下敷きのデザイン)は、ワークテラスさんの色々な提案により当初イメージしていたものよりいい物ができたので、色々な提案や質問は大歓迎です。

また、出来れば今回の依頼の中で、今後も定期的にデザインをお願いできる方がいればという事を兼ねているので、定期的に(大体「月1」位のペース)お願いできる方はその旨お伝えください。

私が選考するポイント
・キャッチやレイアウト等、ターゲットからのレスポンスがありそうか?
私はチラシは如何にして見て読んだ瞬間にアクション(問い合わせ)を起こさせるかがポイントだと思っています。
・レスポンスの速さ(私は速くないですが)等の対応
記載項目
屋号:学習塾 ミナリオ
電話番号:047-513-8847
URL:http://minario-juku.jp/
※ 二次元コードとロゴは添付資料よりおとりください。
サイズ
B4
ページ数
両面
希望イメージ
シンプル 複雑
単色 カラフル
暗い 明るい
日常 高級
遊び心 厳粛
未来的 伝統的
女性的 男性的
希望する色
大きな希望はないですが、塾のイメージはオレンジです。
納品ファイル
• 高解像度JPG (.jpg)
• イラストレーター形式 (.ai)
• フォトショップ形式 (.psd)
補足説明
今回のチラシでは、塾長をある程度前面に出した形にしようと思っているので、
「ここにこんなポーズの写真をいれましょう!」
などのご提案も受け付けます。
言っていただければ、はめ込みもしやすいように白バックで撮ってお渡しします。

また、チラシの依頼は初めてなので説明の足りない箇所等あると思いますので、
その際はお手数ですが、ご質問ください。
キャンペーン面の下部に
「HPに『無料体験者の感想』を掲載しています」
とHPに誘導する仕組みを作成してください。
塾長の写真をアップしました。
ご確認ください。
たくさんのご提案ありがとうございました。
依頼の段階でもお伝えした通り、できれば今後も定期的にお願いできる方が希望です。
定期的な依頼が可能なのに、その旨お伝えいただいていない方はメッセージ等で、その旨ご連絡ください。

選定段階(修正依頼等)に入りましたら、またこの欄にてご報告させていただきます。
(少なくとも金曜日までにはアクションをおこします。)

本当にたくさんのご提案ありがとうございました。
■ 選んだ理由

私の当初のイメージ(熱意がありそう・ちゃんとした塾でありそう)
に、一番近かった事が最大の決め手でした。
また、私が添付したデータはただ腕組みをしている写真でしたが、
動きのある写真の方がいいなぁと、漠然には感じていた所も大きいかと思います。

■ 提案者全員のお礼・コメント

この度は、弊社の依頼にご提案いただき誠にありがとうございました。
正直、選考するのにかなり悩みました。
私が、原案の中で気になっていた箇所をうまくまとめていただいた方、
文言の言い回しの修正の仕方など、とても勉強になりました。
また、依頼をさせていただく際には、是非ご提案いただければと思います。

```html
<!DOCTYPE html>
<html lang="ja">
<head>
<meta charset="utf-8">
<title>中間テスト20点UP保証 | 学習塾 ミナリオ</title>
<link rel="stylesheet" href="https://fonts.googleapis.com/css2?family=Noto+Sans+JP:wght@400;500;700;900&display=swap">
<style>
:root{
  --orange:#f08a1c;
  --orange-deep:#e06a10;
  --red:#d7131d;
  --blue:#1f63b3;
  --blue-dark:#174a8a;
  --ink:#333;
  --white:#fff;
  --paper:#fff;
  --yellow:#fff36b;
}
*{margin:0;padding:0;box-sizing:border-box}
html,body{width:846px;height:1200px;overflow:hidden;background:var(--paper)}
body{font-family:"Noto Sans JP",sans-serif;color:var(--ink)}
.flyer{position:relative;width:846px;height:1200px;overflow:hidden;background:var(--paper)}

.hero-photo{position:absolute;left:0;top:42px;width:846px;height:430px;
  background:linear-gradient(90deg,#f6f4f1 0%,#ece6df 40%,#e4dcd2 60%,#f3f1ee 100%)}
.flash-badge{position:absolute;left:0;top:0;width:196px;height:150px;background:var(--red);
  color:var(--white);font-weight:900;font-size:78px;line-height:150px;text-align:center;letter-spacing:2px}
.target-band{position:absolute;left:196px;top:0;right:0;height:42px;background:var(--blue);
  color:var(--white);font-weight:700;font-size:20px;line-height:42px;text-align:right;padding-right:18px;white-space:nowrap}
.brand{position:absolute;left:650px;top:60px;width:168px;background:var(--white);border:2px solid var(--blue);text-align:center}
.brand-name{display:block;font-weight:900;font-size:36px;color:var(--blue);line-height:62px}
.brand-tag{display:block;background:var(--blue);color:var(--white);font-weight:700;font-size:17px;line-height:30px;letter-spacing:2px}
.catch{position:absolute;left:40px;top:200px;font-weight:700;font-size:36px;line-height:52px;color:var(--ink)}

.guarantee{position:absolute;left:14px;top:465px;width:818px;height:385px;background:var(--orange);
  border:3px solid var(--white);outline:2px solid var(--orange-deep);color:var(--white);text-align:center}
.guarantee-title{font-weight:900;font-size:62px;line-height:70px;margin-top:12px;text-shadow:0 3px 0 var(--orange-deep)}
.guarantee-title.big{font-size:80px;line-height:84px;margin-top:0}
.guarantee-title .up{color:var(--yellow)}
.grades{display:flex;justify-content:center;gap:18px;margin-top:6px}
.grade{width:240px}
.grade-label{display:inline-block;background:var(--blue);color:var(--white);font-weight:700;font-size:16px;padding:0 16px;line-height:24px}
.grade-note{font-size:10px;line-height:14px}
.grade-value{font-weight:900;font-size:34px;line-height:42px}
.refund-lead{font-weight:700;font-size:26px;line-height:36px;margin-top:4px}
.refund{font-weight:900;font-size:28px;line-height:44px;white-space:nowrap}
.refund mark{background:var(--white);color:var(--red);padding:0 8px;border-radius:4px}
.refund .plus{display:inline-block;width:28px;height:28px;line-height:28px;border-radius:50%;background:var(--white);color:var(--orange);font-size:18px;vertical-align:3px}
.guarantee-note{font-size:12px;line-height:18px;margin-top:4px}

.director-photo{position:absolute;left:28px;top:862px;width:270px;height:290px;
  background:linear-gradient(180deg,#e9eef3 0%,#c9d0d8 60%,#8a929c 100%)}
.pitch{position:absolute;left:314px;top:868px;width:350px;font-weight:700;font-size:17px;line-height:28px;color:var(--ink);white-space:nowrap}
.pitch .tag{color:var(--red)}
.recruiting{position:absolute;left:662px;top:894px;width:160px;height:36px;background:var(--orange);color:var(--white);
  font-weight:900;font-size:19px;line-height:36px;text-align:center;border-radius:18px}
.course-title{position:absolute;left:312px;top:940px;font-weight:900;font-size:52px;line-height:76px;color:var(--red);white-space:nowrap}
.course-title ruby rt{font-size:12px;font-weight:700}

.details{position:absolute;left:312px;top:1030px;width:328px;list-style:none;font-size:12px;line-height:20px}
.details li{display:flex;gap:6px;margin-bottom:3px;white-space:nowrap}
.details .key{flex:none;width:64px;background:var(--blue);color:var(--white);text-align:center;font-weight:700}
.apply{position:absolute;left:650px;top:1030px;width:182px;height:122px;border:2px solid var(--blue);font-size:11px;line-height:16px;overflow:hidden}
.apply-head{background:var(--blue);color:var(--white);font-weight:700;font-size:13px;text-align:center;line-height:22px}
.apply-text{padding:4px 6px}
.apply-tel{display:flex;align-items:center;gap:4px;padding:0 6px;font-weight:900;font-size:15px;color:var(--blue-dark);line-height:23px;white-space:nowrap}
.apply-tel .lab{font-size:10px;background:var(--blue);color:var(--white);padding:0 4px;line-height:15px}

.footer{position:absolute;left:0;bottom:0;width:846px;height:42px;background:var(--blue);color:var(--white);
  display:flex;justify-content:space-between;align-items:center;padding:0 20px;font-weight:700;white-space:nowrap}
.footer-msg{font-size:15px}
.footer-url{font-size:21px;font-weight:900}
</style>
</head>
<body>
<main class="flyer">
  <div class="hero-photo" role="img" aria-label="ノートに向かって笑顔を見せる女子中学生の写真"></div>
  <div class="flash-badge">特報</div>
  <div class="target-band">桜ヶ丘台中・若葉中・緑町台中の学生対象、短期特別授業!</div>
  <div class="brand"><span class="brand-name">ミナリオ</span><span class="brand-tag">完全個別指導</span></div>
  <p class="catch">数学嫌いな若者よ、<br>いつまでも<br>逃げちゃダメだ!!</p>

  <section class="guarantee">
    <h1 class="guarantee-title">中間テスト</h1>
    <p class="guarantee-title big">20点UP<span class="up">↑</span>保証</p>
    <div class="grades">
      <div class="grade"><span class="grade-label">1年生</span><p class="grade-note">&nbsp;</p><p class="grade-value">90点保証</p></div>
      <div class="grade"><span class="grade-label">2年生</span><p class="grade-note">1年生の後期期末テストの点数より</p><p class="grade-value">+20点保証</p></div>
      <div class="grade"><span class="grade-label">3年生</span><p class="grade-note">2年生の後期期末テストの点数より</p><p class="grade-value">+20点保証</p></div>
    </div>
    <p class="refund-lead">もし、点数が上がらなかったら</p>
    <p class="refund">授業料は <mark>全額返還</mark> + <span class="plus">無</span><mark>補習授業</mark> を行います。</p>
    <p class="guarantee-note">※保証の適用には全日程の出席と課題の提出が必要です。詳しくはお問い合わせください。</p>
  </section>

  <div class="director-photo" role="img" aria-label="指を差して呼びかける塾長の写真"></div>
  <p class="pitch"><span class="tag">〈定期テスト対策塾〉</span>ミナリオがみせる、<br>本物の指導力!</p>
  <div class="recruiting">受講生募集中</div>
  <h2 class="course-title">塾長直伝『<ruby>中間<rt>ちゅうかん</rt>特講<rt>とっこう</rt></ruby>』</h2>

  <ul class="details">
    <li><span class="key">対象校</span>桜ヶ丘台中・若葉中・緑町台中の生徒</li>
    <li><span class="key">科目</span>中学数学(中間テスト範囲を集中指導)</li>
    <li><span class="key">日程</span>テスト前の二週間・全六回の特別授業</li>
    <li><span class="key">定員</span>各学年先着十名まで(定員になり次第締切)</li>
    <li><span class="key">費用</span>教材費込み・詳しくは塾までお尋ねください</li>
  </ul>

  <aside class="apply">
    <p class="apply-head">お申込方法</p>
    <p class="apply-text">お電話または来塾にてお申込みください。受付は平日午後です。</p>
    <p class="apply-tel">
      <svg width="13" height="13" viewBox="0 0 24 24" aria-hidden="true"><path fill="#174a8a" d="M6.6 10.8a15 15 0 006.6 6.6l2.2-2.2a1 1 0 011-.25 11.4 11.4 0 003.6.57 1 1 0 011 1V20a1 1 0 01-1 1A17 17 0 013 4a1 1 0 011-1h3.5a1 1 0 011 1c0 1.25.2 2.45.57 3.57a1 1 0 01-.25 1z"/></svg>
      <span class="lab">TEL</span>047-513-8847</p>
    <p class="apply-tel"><svg width="13" height="13" viewBox="0 0 24 24" aria-hidden="true"></svg><span class="lab">FAX</span>047-513-8848</p>
  </aside>

  <footer class="footer">
    <span class="footer-msg">ホームページで『無料体験者の感想』を掲載しています</span>
    <span class="footer-url">http://minario-juku.jp/</span>
  </footer>
</main>
</body>
</html>
```